Movie poster for drama/thriller feature

We need a movie poster for an edgy microbudget, drama/thriller feature called Stumbling My Road Past Dawn and is about a “night in the life” of an escort and her driver after she discovers that her mother, who was caring for her daughter, has died. She has just one night to raise the money to cover the arrears on her mother’s mortgage and return to collect her daughter before her very religious aunt calls Children’s Aid. On top of that she has to enlist the help of her new driver who is also very religious and hates her because she’s a “whore”. He is only doing this job because, as a Cuban refugee, he has had to take a job with his uncle, who is head of security at the agency, in order to pay him back what it cost to bring him to Canada. So, at the core of the story is this relationship between two people who hate each other but are stuck together in a car for an entire night. The third character is the uncle - head of security - who becomes increasingly "dark" and violent as the night goes on as he feels he is losing the loyalty of his nephew to a sex worker who is ripping off his boss.

So, that's the backdrop to the story.

Now, we want the poster to reflect that this is a scrappy, edgy little film, a bit controversial (just the title alone, obviously). Some of our inspiration for the poster are the kind of minimalist designs from French New Wave films (examples uploaded). The title itself can either be written out in toto or you could put the acronym in bold letters - SMRPD - with their meaning smaller below it. You can play with it, anyway, to come up with some cool. I've also included stills from the film of the three main characters - Marisol, the lead/star, Tomas (her driver) and Ignacio, the antaonist/uncle. You can crop these to make them work. I just left them full size so that you'd have more options.

If you have questions, don't hesitate to ask.

best
Derek

Target Market(s)

indie film goers, younger, city-based, hipster demographic

Industry/Entity Type

Film Production

Font styles to use
Sans Serif

Colors

Designer to choose colors to be used in the design.

Requirements
Must have
• A great look, the title, and some credits:
• tagline: one night can change your whole world
• A film by Bridget Oldcastle & Derek Fenwold
• With
• Ingrid Tolmachova
• Esteban Morales-Quiroga
• Raul Caceres Villalobos
• Cinematography
• Nate Corbell
• Produced by:
• Crooked Lantern Productions
• Pinecrest Studios
• and a credit block with:
• Bridget Oldcastle ... co-producer
• Ingrid Tolmachova ... co-producer
• Esteban Morales-Quiroga ... co-producer
• Gavin Trout ... co-producer
• Derek Fenwold ... co-producer
• Editing by
• Dana McGivney
• Production Design by
• Tiago Mendes Rocha
• Wendy Calder ... key makeup artist
• Priscilla Novak ... makeup artist Production Management
• Tessa Kimball ... production manager Second Unit Director or Assistant Director
• Tessa Kimball ... first assistant director Sound Department
• Ben Yardley ... sound editor
• Kevin Santoso ... sound recordist Stunts
• Raul Caceres Villalobos ... action coordinator
• Carl Pembry ... still photographer
• Fiona Beckett ... swing
• Monica Thorne ... still photographer
• Giulia Marchetti ... swing Costume and Wardrobe Department
• Nora Fairclough ... wardrobe
• Petra Holub ... wardrobe supervisor Transportation Department
• Rosalind Tapley ... craft service
• Maya Finch ... script supervisor
• Paolo Reyes ... production assistant
• Lucia Navarro ... craft service

```html
<!DOCTYPE html>
<html lang="en">
<head>
<meta charset="utf-8">
<title>Stumbling My Road Past Dawn</title>
<link href="https://fonts.googleapis.com/css2?family=Anton&family=Oswald:wght@400;500;600;700&family=Archivo+Black&display=swap" rel="stylesheet">
<style>
  :root {
    --ink: #000;
    --white: #fff;
    --tag-yellow: #f6d52c;
    --tag-cream: #fff7cf;
    --night-teal: #2d5a60;
    --dash-violet: #6a4a80;
    --wash-pink: #e7a6c8;
    --wash-green: #3fa870;
    --wash-magenta: #c0407e;
  }
  * { margin: 0; padding: 0; box-sizing: border-box; }
  html, body { width: 800px; height: 1200px; overflow: hidden; background: var(--ink); }
  .poster { position: relative; width: 800px; height: 1200px; overflow: hidden; background: var(--ink); }

  .backdrop {
    position: absolute; inset: 0 0 240px 0;
    background:
      radial-gradient(ellipse 220px 260px at 520px 700px, rgba(214,170,150,.55), transparent 70%),
      radial-gradient(ellipse 200px 120px at 250px 640px, rgba(90,170,175,.55), transparent 70%),
      radial-gradient(ellipse 420px 90px at 400px 880px, rgba(160,100,170,.7), transparent 75%),
      linear-gradient(180deg, var(--wash-pink) 0%, #b56b9a 10%, #6d5f7a 22%, #2b2230 45%, var(--night-teal) 58%, #1d1a22 72%, var(--dash-violet) 80%, #1a1018 92%, var(--ink) 100%);
  }
  .backdrop::before {
    content: ""; position: absolute; left: 380px; top: 0; width: 200px; height: 160px;
    background: radial-gradient(ellipse at center, rgba(63,168,112,.8), transparent 70%);
  }
  .backdrop::after {
    content: ""; position: absolute; right: 0; top: 0; width: 240px; height: 170px;
    background: radial-gradient(ellipse at 70% 20%, rgba(192,64,126,.8), transparent 70%);
  }

  .tagline { position: absolute; top: 40px; left: 0; width: 800px; height: 60px; }

  .title-mark { position: absolute; left: 0; top: 105px; width: 800px; height: 560px; }

  .title-words {
    position: absolute; left: 0; top: 672px; width: 800px; text-align: center;
    font-family: "Oswald", sans-serif; font-weight: 600; font-size: 22px; line-height: 1;
    letter-spacing: 9px; text-transform: uppercase; color: var(--white);
  }

  .credits {
    position: absolute; left: 0; top: 948px; width: 800px; text-align: center;
    font-family: "Oswald", sans-serif; color: var(--white); text-transform: uppercase;
  }
  .credits p { line-height: 1; white-space: nowrap; }
  .credits .directors { font-size: 19px; font-weight: 500; text-transform: none; margin-bottom: 4px; }
  .credits .directors b { font-family: "Archivo Black", sans-serif; font-weight: 400; text-transform: uppercase; font-size: 17px; }
  .credits .cast { font-size: 18px; font-weight: 500; margin-bottom: 4px; word-spacing: 2px; }
  .credits .cast .role { text-transform: none; }
  .credits .block { font-size: 15px; font-weight: 500; margin-bottom: 6px; }
  .credits .role-sm { font-size: 7px; font-weight: 500; vertical-align: 6px; margin: 0 2px; }
</style>
</head>
<body>
<main class="poster">
  <div class="backdrop" role="img" aria-label="Night-time photograph of the lead actress seated in a car, lit by blurred city lights and a hanging cross on the mirror"></div>

  <svg class="tagline" viewBox="0 0 800 60" aria-label="One night can change your whole world">
    <text x="400" y="50" text-anchor="middle" textLength="784" lengthAdjust="spacingAndGlyphs"
          font-family="Oswald, sans-serif" font-weight="700" font-size="50"
          stroke="var(--ink)" stroke-width="5" paint-order="stroke" stroke-linejoin="round">
      <tspan fill="var(--tag-cream)">ONE NIGHT </tspan><tspan fill="var(--tag-yellow)">CAN CHANGE YOUR </tspan><tspan fill="var(--tag-cream)">WHOLE WORLD</tspan>
    </text>
  </svg>

  <svg class="title-mark" viewBox="0 0 800 560" role="img" aria-label="SMRPD title letters filled with stills of the three leads and stacks of cash">
    <defs>
      <linearGradient id="letter-fill" x1="0" y1="0" x2="800" y2="0" gradientUnits="userSpaceOnUse">
        <stop offset="0" stop-color="#a07a55"/>
        <stop offset=".15" stop-color="#8a5a3c"/>
        <stop offset=".2" stop-color="#b3262c"/>
        <stop offset=".34" stop-color="#5a1a1e"/>
        <stop offset=".42" stop-color="#1c1c22"/>
        <stop offset=".6" stop-color="#2a2630"/>
        <stop offset=".72" stop-color="#3d3a3e"/>
        <stop offset=".84" stop-color="#9c8a6a"/>
        <stop offset="1" stop-color="#c8b890"/>
      </linearGradient>
    </defs>
    <text x="400" y="552" text-anchor="middle" font-family="Anton, sans-serif" font-size="628"
          textLength="784" lengthAdjust="spacingAndGlyphs" fill="url(#letter-fill)" fill-opacity=".92">SMRPD</text>
  </svg>

  <p class="title-words">Stumbling My Road Past Dawn</p>

  <section class="credits">
    <p class="directors">A film by <b>Bridget Oldcastle &amp; Derek Fenwold</b></p>
    <p class="cast"><span class="role">with</span> Ingrid Tolmachova &nbsp;Esteban Morales-Quiroga &nbsp;Raul Caceres Villalobos</p>
    <p class="cast"><span class="role">Cinematography</span> Nate Corbell <span class="role">Produced by</span> Crooked Lantern Productions Pinecrest Studios</p>
    <p class="block"><span class="role-sm">Co-producer</span> Bridget Oldcastle &nbsp;Ingrid Tolmachova &nbsp;Esteban Morales-Quiroga &nbsp;Gavin Trout &nbsp;Derek Fenwold</p>
    <p class="block"><span class="role-sm">Editing by</span> Dana McGivney <span class="role-sm">Production design by</span> Tiago Mendes Rocha <span class="role-sm">Key makeup artist</span> Wendy Calder</p>
    <p class="block"><span class="role-sm">Makeup artist production management</span> Priscilla Novak <span class="role-sm">Production manager second unit director or assistant director</span> Tessa Kimball</p>
    <p class="block"><span class="role-sm">First assistant director sound department</span> Tessa Kimball <span class="role-sm">Sound editor</span> Ben Yardley <span class="role-sm">Sound recordist stunts</span> Kevin Santoso</p>
    <p class="block"><span class="role-sm">Action coordinator</span> Raul Caceres Villalobos <span class="role-sm">Still photographer</span> Carl Pembry Monica Thorne <span class="role-sm">Swing</span> Fiona Beckett</p>
    <p class="block"><span class="role-sm">Swing costume and wardrobe department</span> Giulia Marchetti <span class="role-sm">Wardrobe</span> Nora Fairclough <span class="role-sm">Wardrobe supervisor transportation department</span> Petra Holub <span class="role-sm">Craft service</span> Rosalind</p>
    <p class="block">Tapley <span class="role-sm">Script supervisor</span> Maya Finch <span class="role-sm">Production assistant</span> Paolo Reyes <span class="role-sm">Craft service</span> Lucia Navarro</p>
  </section>
</main>
</body>
</html>
```